Real Estate Development and Brokerage Middle East

Required is a web site design for a new branch of an existing Real Estate Development and Brokerage company. The Branch will be established in the United Arab Emirates - Veluna Middle East, the mother company is based in Austria/Europe. The new branch focuses on the middle eastern clients such as Institutional Investors/Family Businesses/Wealthy Individuals looking either for a luxury home in Vienna City or the alpine nature or are interested to invest in ready made properties or real estate development projects in Austria run by the branches mother co. in Austria. The design should highlight both Services i.e. Investment for commercial purpose and for residential purposes (focus on the nature) as well as the companies focus on high end luxury selected properties only and having middle east experienced staff in the UAE.

The link to the Austrian HQ website is below: Design elements of that website might or might not be used, however the logo shall be the same.
http://plenodraft.example/QW7RTZMBX

Attached the logo and a rough first draft of the structure of the website (not yet set in stone) . The attachment contains also a link to a website of a company in a similar industry. I do like the way they present the highlights on their start/home page. The boxes. By the way, we believe that more graphic (pictures) and a bit less text might be a good way to approach our future target customers.

As we hope to sell many of the projects and hence many new projects descriptions/pictures will be uploaded in future on an ongoing basis the page should have the ability to upload information and pics by our team (none of it is a web designer and has experience exceeding MS-Office).

Lastly - and for the future we might need (not sure yet) need the entire context in Arabic (the language button)

Thanks.
Lars

Target Market(s)

Institutional Investors and wealthy individuals / family offices

Industry/Entity Type

Real Estate

Coding

Number of Pages Required

5+ page

Requirements
Must have
• Same Logo as Parent Company
Nice to have
• News ticker/banner, high resolution picture heavy, changing pictures on start/home page, PDF downloads

```html
<!DOCTYPE html>
<html lang="en">
<head>
<meta charset="utf-8">
<title>Veluna Middle East – Real Estate</title>
<link rel="stylesheet" href="https://fonts.googleapis.com/css2?family=Open+Sans:wght@400;600;700&family=Oswald:wght@300;400;600&display=swap">
<style>
:root{
  --blue:#5a7fa6;
  --blue-dark:#3e5f82;
  --blue-deep:#2c4663;
  --blue-pale:#d7e2ee;
  --grey-bg:#eef0f2;
  --grey-line:#d6d9dc;
  --text:#555b61;
  --text-dark:#2f3338;
  --white:#ffffff;
  --accent:#c0504d;
  --ticker:#3a3d42;
}
*{box-sizing:border-box;margin:0;padding:0}
html,body{width:720px;height:1200px;overflow:hidden}
body{font-family:"Open Sans",Arial,sans-serif;color:var(--text);background:var(--white);position:relative;font-size:8px;line-height:1.45}
.abs{position:absolute}

/* header */
.site-header{position:absolute;left:0;top:0;width:720px;height:56px;background:var(--white);border-bottom:1px solid var(--grey-line)}
.brand{position:absolute;left:40px;top:14px;display:flex;align-items:center;gap:8px}
.brand-mark{width:22px;height:22px;background:var(--blue-dark)}
.brand-name{font-family:"Open Sans",Arial,sans-serif;font-weight:700;font-size:17px;color:var(--blue-dark);letter-spacing:.3px}
.lang-flag{position:absolute;left:566px;top:8px;width:14px;height:9px;background:var(--blue-dark)}
.lang-label{position:absolute;left:584px;top:6px;font-size:7px;color:var(--text)}
.main-nav{position:absolute;left:420px;top:30px;display:flex;gap:0}
.main-nav a{display:block;padding:0 11px;font-size:7.5px;font-weight:600;color:var(--text-dark);text-decoration:none;line-height:22px}
.main-nav a.active{background:var(--blue-dark);color:var(--white)}

/* hero */
.hero{position:absolute;left:0;top:56px;width:720px;height:364px;background:linear-gradient(180deg,#9fb7cc 0%,#b9c8d4 35%,#8d97a0 62%,#c6b79d 82%,#9aa7ae 100%)}
.hero-title{position:absolute;left:58px;top:80px;font-family:"Oswald",Arial,sans-serif;font-weight:600;font-size:30px;color:var(--white);letter-spacing:.5px}
.hero-sub{position:absolute;left:58px;top:124px;padding:4px 10px;background:rgba(62,95,130,.85);font-family:"Oswald",Arial,sans-serif;font-weight:300;font-size:17px;color:var(--white)}
.hero-arrow{position:absolute;top:134px;width:22px;height:30px;background:rgba(44,70,99,.75)}
.hero-dots{position:absolute;left:300px;top:294px;display:flex;gap:5px}
.hero-dots span{width:6px;height:6px;border-radius:50%;background:rgba(255,255,255,.6)}
.hero-dots span.on{background:var(--white)}

.search-panel{position:absolute;left:566px;top:76px;width:130px;height:210px;background:rgba(90,127,166,.88);padding:10px 9px}
.search-panel h3{font-family:"Oswald",Arial,sans-serif;font-weight:400;font-size:11px;color:var(--white);text-align:center;margin-bottom:8px}
.field{height:16px;background:var(--white);margin-bottom:6px;font-size:7px;line-height:16px;padding-left:5px;color:var(--text);position:relative}
.field::after{content:"";position:absolute;right:5px;top:6px;border:3px solid transparent;border-top-color:var(--text)}
.field-row{display:flex;gap:5px}
.field-row .field{flex:1}
.search-btn{margin-top:4px;height:20px;background:var(--blue-deep);color:var(--white);font-size:7.5px;text-align:center;line-height:20px;font-weight:600}

/* feature boxes */
.features{position:absolute;left:66px;top:380px;display:flex;gap:24px}
.feature{width:180px;height:160px;background:var(--white);border:1px solid var(--grey-line);position:relative;text-align:center;padding-top:40px}
.feature-icon{position:absolute;left:68px;top:-24px;width:44px;height:44px;border-radius:50%;background:var(--blue-dark);border:3px solid var(--white);display:flex;align-items:center;justify-content:center}
.feature h4{font-family:"Open Sans",Arial,sans-serif;font-weight:600;font-size:10px;color:var(--text-dark);margin-bottom:5px}
.feature p{font-size:6.5px;padding:0 16px;color:var(--text)}
.read-bar{position:absolute;left:0;bottom:0;width:100%;height:20px;background:var(--blue);color:var(--white);font-size:6.5px;font-weight:600;line-height:20px;text-align:center}

/* about */
.section-title{font-family:"Oswald",Arial,sans-serif;font-weight:400;font-size:17px;color:var(--blue)}
.section-tag{font-size:7px;font-style:italic;color:var(--text)}
.about{position:absolute;left:40px;top:556px;width:640px}
.about-rule{height:1px;background:var(--grey-line);margin:6px 0 14px}
.about-photo{position:absolute;left:22px;top:60px;width:96px;height:96px;border-radius:50%;border:4px solid var(--grey-bg);background:radial-gradient(circle at 50% 40%,#c9b89c 0%,#8f7c64 60%,#5d5044 100%)}
.about-text{position:absolute;left:150px;top:62px;width:480px;font-size:7px}
.btn-dark{display:inline-block;margin-top:10px;background:var(--blue-deep);color:var(--white);font-size:6.5px;font-weight:600;padding:4px 10px}

/* pdf band */
.pdf-band{position:absolute;left:0;top:780px;width:720px;height:46px;background:var(--blue)}
.pdf-icon{position:absolute;left:44px;top:10px;width:20px;height:26px;background:var(--white)}
.pdf-text{position:absolute;left:76px;top:9px;width:440px;font-size:6.5px;color:var(--white)}
.pdf-btn{position:absolute;left:556px;top:13px;width:122px;height:20px;background:var(--white);color:var(--text-dark);font-size:7px;font-weight:700;line-height:20px;text-align:center;border-left:8px solid var(--accent)}

/* properties */
.properties{position:absolute;left:0;top:846px;width:720px;text-align:center}
.properties .section-tag{margin-top:3px}
.prop-cards{position:absolute;left:60px;top:900px;display:flex;gap:15px}
.prop-card{width:190px;height:186px;background:var(--white);border:1px solid var(--grey-line)}
.prop-photo{height:108px}
.prop-caption{height:24px;background:var(--blue-dark);color:var(--white);display:flex;justify-content:space-between;align-items:center;padding:0 8px}
.prop-caption b{font-family:"Oswald",Arial,sans-serif;font-weight:400;font-size:10px}
.prop-caption span{font-size:6px}
.prop-card p{font-size:6.5px;padding:6px 8px 0;text-align:left}
.prop-card .more{font-size:6px;color:var(--blue-dark);font-weight:700;padding:3px 8px;text-align:left}
.prop-arrow{position:absolute;top:980px;width:12px;height:26px;background:var(--grey-line)}
.prop-dots{position:absolute;left:336px;top:1094px;display:flex;gap:5px}
.prop-dots span{width:6px;height:6px;border-radius:50%;background:var(--grey-line)}
.prop-dots span.on{background:var(--blue-dark)}

/* news */
.news{position:absolute;left:40px;top:1106px}
.news-band{position:absolute;left:40px;top:1142px;width:640px;height:26px;background:var(--ticker)}
.news-label{position:absolute;left:0;top:0;width:46px;height:26px;background:var(--blue-deep);color:var(--white);font-family:"Oswald",Arial,sans-serif;font-size:9px;line-height:26px;text-align:center}
.news-text{position:absolute;left:56px;top:4px;width:560px;font-size:6px;color:#d8dbe0;line-height:1.5}

/* footer */
.site-footer{position:absolute;left:0;top:1176px;width:720px;height:24px;background:var(--grey-bg);border-top:1px solid var(--grey-line)}
.site-footer small{position:absolute;left:40px;top:7px;font-size:6px;color:var(--text)}
.social{position:absolute;right:40px;top:5px;display:flex;gap:4px}
.social span{width:13px;height:13px;border-radius:50%;background:var(--blue-dark)}
</style>
</head>
<body>

<header class="site-header">
  <div class="brand"><span class="brand-mark"></span><span class="brand-name">Veluna Immobilien</span></div>
  <span class="lang-flag"></span><span class="lang-label">EN</span>
  <nav class="main-nav">
    <a class="active">HOME</a><a>ABOUT</a><a>SERVICES &amp; NEWS</a><a>REFERENCES</a><a>CONTACT US</a>
  </nav>
</header>

<section class="hero" role="img" aria-label="City skyline with high-rise towers above a waterfront beach">
  <h1 class="hero-title">WE DENOUNCE WITH RIGHTEOUS</h1>
  <div class="hero-sub">Denouncing pleasure and praising pain idiotique...</div>
  <div class="hero-arrow" style="left:14px">
    <svg width="22" height="30"><path d="M13 9 L8 15 L13 21" stroke="#fff" stroke-width="2" fill="none"/></svg>
  </div>
  <div class="hero-arrow" style="left:684px">
    <svg width="22" height="30"><path d="M9 9 L14 15 L9 21" stroke="#fff" stroke-width="2" fill="none"/></svg>
  </div>
  <div class="hero-dots"><span class="on"></span><span></span><span></span><span></span></div>
</section>

<form class="search-panel">
  <h3>Find Your Home</h3>
  <div class="field">Location</div>
  <div class="field">Type</div>
  <div class="field-row"><div class="field">Beds</div><div class="field">Baths</div></div>
  <div class="field-row"><div class="field">Price From</div><div class="field">Price To</div></div>
  <div class="field">Status</div>
  <div class="search-btn">Search and Have Now</div>
</form>

<div class="features">
  <article class="feature">
    <div class="feature-icon">
      <svg width="22" height="20" viewBox="0 0 22 20"><path d="M11 1 L21 10 H18 V19 H13 V13 H9 V19 H4 V10 H1 Z" fill="#fff"/></svg>
    </div>
    <h4>Best Home</h4>
    <p>Sed ut perspiciatis unde omnis iste natus error sit voluptatem accusantium doloremque laudantium totam rem.</p>
    <div class="read-bar">READ MORE ›</div>
  </article>
  <article class="feature">
    <div class="feature-icon">
      <svg width="22" height="22" viewBox="0 0 22 22"><text x="11" y="17" text-anchor="middle" font-family="Open Sans, Arial, sans-serif" font-size="18" font-weight="700" fill="#fff">$</text></svg>
    </div>
    <h4>Best Prices</h4>
    <p>Nemo enim ipsam voluptatem quia voluptas sit aspernatur aut odit aut fugit sed quia consequuntur magni dolores.</p>
    <div class="read-bar">READ MORE ›</div>
  </article>
  <article class="feature">
    <div class="feature-icon">
      <svg width="24" height="22" viewBox="0 0 24 22"><circle cx="9" cy="12" r="6" fill="none" stroke="#fff" stroke-width="3" stroke-dasharray="3 2"/><circle cx="9" cy="12" r="2" fill="#fff"/><circle cx="18" cy="6" r="4" fill="none" stroke="#fff" stroke-width="2.4" stroke-dasharray="2 1.6"/></svg>
    </div>
    <h4>Free Support</h4>
    <p>Neque porro quisquam est qui dolorem ipsum quia dolor sit amet consectetur adipisci velit sed quia non numquam.</p>
    <div class="read-bar">READ MORE ›</div>
  </article>
</div>

<section class="about">
  <h2 class="section-title">ABOUT US</h2>
  <p class="section-tag">Deeply dummy text of the printing and typesetting industry. Lorem Ipsum has been the industry's standard dummy text ever since...</p>
  <div class="about-rule"></div>
  <div class="about-photo" role="img" aria-label="Round photo of a luxury residence interior"></div>
  <div class="about-text">
    <p>Sed ut perspiciatis unde omnis iste natus error sit voluptatem accusantium doloremque laudantium, totam rem aperiam, eaque ipsa quae ab illo inventore veritatis et quasi architecto beatae vitae dicta sunt explicabo. Nemo enim ipsam voluptatem quia voluptas sit aspernatur aut odit aut fugit, sed quia consequuntur magni dolores eos qui ratione voluptatem sequi nesciunt. Neque porro quisquam est, qui dolorem ipsum quia dolor sit amet, consectetur, adipisci velit, sed quia non numquam eius modi tempora incidunt ut labore et dolore magnam aliquam quaerat voluptatem.</p>
    <span class="btn-dark">READ MORE</span>
  </div>
</section>

<section class="pdf-band">
  <span class="pdf-icon"></span>
  <p class="pdf-text">The complete investment brochure with detailed project descriptions, floor plans and market figures for our residential and commercial portfolio in Vienna and the Alps is available as a document for download. Please register to receive future updates.</p>
  <span class="pdf-btn">CLICK TO DOWNLOAD</span>
</section>

<section class="properties">
  <h2 class="section-title">PROPERTIES</h2>
  <p class="section-tag">Deeply dummy text of the printing and typesetting industry. Lorem Ipsum has been the industry's standard dummy text ever since...</p>
</section>

<span class="prop-arrow" style="left:40px"></span>
<span class="prop-arrow" style="left:668px"></span>
<div class="prop-cards">
  <article class="prop-card">
    <div class="prop-photo" role="img" aria-label="Bright living room with white sofas" style="background:linear-gradient(135deg,#e9e6e1,#b9b2a8 55%,#6f6a64)"></div>
    <div class="prop-caption"><b>Sed ut perspiciatis</b><span>22 March 2015</span></div>
    <p>Unde omnis iste natus error sit voluptatem accusantium doloremque laudantium totam rem.</p>
    <div class="more">READ MORE ›</div>
  </article>
  <article class="prop-card">
    <div class="prop-photo" role="img" aria-label="Modern bedroom with dark wood furniture" style="background:linear-gradient(135deg,#d8d4cf,#8a7d70 55%,#3f3a36)"></div>
    <div class="prop-caption"><b>Sed ut perspiciatis</b><span>22 March 2015</span></div>
    <p>Nemo enim ipsam voluptatem quia voluptas sit aspernatur aut odit aut fugit sed quia.</p>
    <div class="more">READ MORE ›</div>
  </article>
  <article class="prop-card">
    <div class="prop-photo" role="img" aria-label="Open kitchen and dining area in black and white" style="background:linear-gradient(135deg,#f1f1f1,#a7a9ab 50%,#2f3136)"></div>
    <div class="prop-caption"><b>Sed ut perspiciatis</b><span>22 March 2015</span></div>
    <p>Neque porro quisquam est qui dolorem ipsum quia dolor sit amet consectetur adipisci velit.</p>
    <div class="more">READ MORE ›</div>
  </article>
</div>
<div class="prop-dots"><span class="on"></span><span></span><span></span></div>

<section class="news">
  <h2 class="section-title">NEWS TICKER</h2>
  <p class="section-tag">Deeply dummy text of the printing and typesetting industry. Lorem Ipsum has been the industry's standard dummy text ever since...</p>
</section>
<div class="news-band">
  <span class="news-label">NEWS</span>
  <p class="news-text">New alpine residence project released for pre-sale this spring, featuring twelve private chalets with panoramic mountain views and full concierge service. Vienna city portfolio expanded with two historic buildings now open for institutional investment.</p>
</div>

<footer class="site-footer">
  <small>Copyright © 2015 Veluna Middle East. All Rights Reserved.</small>
  <div class="social"><span></span><span></span><span></span></div>
</footer>

</body>
</html>
```